Flyer design for Commcercial building painting services company

I want to design a double sided A4 colour flyer to describe our professional painting services for commercial and industrial buildings.

the list of services is as follows.

Painting to internal common areas, carparks and foyers
Painting to external facades
Carpark and loading dock linemarking and epoxy flooring
Non slip walkways for pedestrian and vehicle traffic
Speed humps, bollard installation.
Non structural building, maintenance and repairs.

Please include some photos of the various services as painting is a visual business.
Design guide can be referenced at www.brushlinecoatings.com.au

```html
<!DOCTYPE html>
<html lang="en">
<head>
<meta charset="utf-8">
<title>Brushline Coatings – Flyer Front and Back</title>
<link rel="stylesheet" href="https://fonts.googleapis.com/css2?family=Montserrat:wght@300;400;500;700;800&family=Nunito:wght@500;600&display=swap">
<style>
  :root{
    --stage:#8a8a8a;
    --white:#ffffff;
    --blue-deep:#1b5aa9;
    --blue-mid:#2277c8;
    --blue-bright:#29a9e1;
    --navy:#1b2c5b;
    --yellow:#f6d823;
    --ink:#2f3440;
    --brand-text:#1f4f9a;
    --card-line:#2a8fd6;
    --paper:#f3f5f8;
  }
  *{margin:0;padding:0;box-sizing:border-box}
  html,body{width:1200px;height:990px;overflow:hidden;background:var(--stage)}
  body{position:relative;font-family:"Montserrat",sans-serif}
  .side-label{position:absolute;top:153px;width:300px;text-align:center;color:var(--white);font-weight:800;font-size:27px;letter-spacing:1px}
  .side-label.front{left:213px}
  .side-label.back{left:730px}
  .flyer{position:absolute;top:196px;width:486px;height:630px;overflow:hidden;background:var(--white)}
  .flyer.front{left:100px}
  .flyer.back{left:628px}
  .flyer > svg.art{position:absolute;left:0;top:0;width:486px;height:630px}
  .brand{position:absolute;display:flex;align-items:flex-start}
  .brand-mark{background:var(--blue-deep);flex:none}
  .brand-name{position:absolute;color:var(--brand-text);font-weight:400;white-space:nowrap}
  .brand-tag{position:absolute;color:var(--brand-text);font-weight:400;white-space:nowrap}

  .welcome{position:absolute;left:33px;top:466px;color:var(--white)}
  .welcome .lead{font-weight:300;font-size:22px;letter-spacing:1px;line-height:26px}
  .welcome .name{font-weight:800;font-size:31px;line-height:33px}
  .welcome .name.accent{color:var(--yellow)}
  .service-area{position:absolute;left:338px;top:494px;color:var(--white);font-size:12px;line-height:15px;font-weight:400}
  .service-area strong{display:block;font-weight:700;font-size:11.5px;margin-bottom:1px}
  .divider{position:absolute;left:316px;top:472px;width:1px;height:100px;background:rgba(255,255,255,.22)}

  .footer-item{position:absolute;top:600px;color:var(--white);font-size:13px;line-height:18px;display:flex;align-items:center;gap:5px;white-space:nowrap}
  .footer-item b{font-weight:700}
  .footer-item svg{width:12px;height:12px;flex:none}

  .services-title{position:absolute;left:27px;top:76px;color:var(--white);font-size:20px;line-height:23px;font-weight:500}
  .services-title b{font-weight:800}
  .services-title .accent{color:var(--yellow);font-weight:800;display:block}
  .services-title .pointer{display:block;width:0;height:0;margin-top:6px;margin-left:1px;border-left:6px solid transparent;border-right:6px solid transparent;border-top:6px solid var(--yellow)}
  .service-card{position:absolute;width:128px;height:117px;border:1.5px solid var(--card-line);border-radius:7px;background:rgba(255,255,255,.78)}
  .service-icon{position:absolute;left:36px;top:-26px;width:54px;height:54px;border-radius:50%;background:linear-gradient(160deg,var(--blue-bright),var(--blue-deep));border:2px solid var(--white);display:flex;align-items:center;justify-content:center}
  .service-icon svg{width:30px;height:30px;fill:none;stroke:var(--white);stroke-width:1.6;stroke-linecap:round;stroke-linejoin:round}
  .service-text{position:absolute;left:12px;right:12px;top:41px;text-align:center;font-family:"Nunito",sans-serif;font-weight:600;font-size:11.4px;line-height:13px;color:var(--ink)}
  .brand-panel{position:absolute;left:38px;top:499px;width:265px;height:63px;background:rgba(255,255,255,.92)}
</style>
</head>
<body>

<div class="side-label front">FRONT</div>
<div class="side-label back">BACK</div>

<!-- FRONT SIDE -->
<section class="flyer front">
  <svg class="art" viewBox="0 0 852 1104" preserveAspectRatio="none">
    <defs>
      <linearGradient id="frontBlue" x1="0" y1="0" x2="1" y2="0.3">
        <stop offset="0" stop-color="#1b56a4"/>
        <stop offset="1" stop-color="#2aaae2"/>
      </linearGradient>
      <linearGradient id="ph1" x1="0" y1="0" x2="1" y2="1"><stop offset="0" stop-color="#2c5fb0"/><stop offset=".55" stop-color="#e8e8ea"/><stop offset="1" stop-color="#c9242c"/></linearGradient>
      <linearGradient id="ph2" x1="0" y1="0" x2="1" y2="1"><stop offset="0" stop-color="#d8d9dc"/><stop offset=".6" stop-color="#9a9ca0"/><stop offset="1" stop-color="#3a3b3e"/></linearGradient>
      <linearGradient id="ph3" x1="0" y1="0" x2="1" y2="1"><stop offset="0" stop-color="#8ea4bf"/><stop offset=".5" stop-color="#6d6b62"/><stop offset="1" stop-color="#c9ad2a"/></linearGradient>
      <linearGradient id="ph4" x1="0" y1="0" x2="1" y2="1"><stop offset="0" stop-color="#2b66c0"/><stop offset=".5" stop-color="#c8cdd4"/><stop offset="1" stop-color="#b5262d"/></linearGradient>
      <linearGradient id="ph5" x1="0" y1="0" x2="1" y2="1"><stop offset="0" stop-color="#e6e8ea"/><stop offset=".6" stop-color="#b7babd"/><stop offset="1" stop-color="#8d8f92"/></linearGradient>
      <linearGradient id="ph6" x1="0" y1="0" x2="1" y2="1"><stop offset="0" stop-color="#d9d4c6"/><stop offset=".5" stop-color="#a9a49a"/><stop offset="1" stop-color="#6f6c66"/></linearGradient>
    </defs>
    <rect width="852" height="1104" fill="url(#frontBlue)"/>
    <polygon points="0,0 852,0 852,705 554,830 0,598" fill="#fff"/>
    <polygon points="0,175 305,168 305,180 0,205" fill="#1f6cc0"/>
    <polygon points="561,232 852,82 852,122 561,246" fill="#2490d8"/>
    <polygon role="img" aria-label="Photo: freshly painted commercial building facade in red, white and blue" points="0,205 305,180 305,445 0,465" fill="url(#ph1)"/>
    <polygon role="img" aria-label="Photo: worker rolling epoxy coating on a warehouse floor" points="0,475 305,455 305,702 0,588" fill="url(#ph2)"/>
    <polygon role="img" aria-label="Photo: yellow hatched linemarking on a rail-side roadway" points="319,182 549,237 549,537 319,457" fill="url(#ph3)"/>
    <polygon role="img" aria-label="Photo: apartment block with red and blue painted walls" points="319,467 549,547 549,807 319,742" fill="url(#ph4)"/>
    <polygon role="img" aria-label="Photo: painter on an elevated boom lift beside a warehouse wall" points="561,240 852,95 852,417 561,537" fill="url(#ph5)"/>
    <polygon role="img" aria-label="Photo: worker sanding a floor edge inside a building" points="561,547 852,430 852,697 561,807" fill="url(#ph6)"/>
    <path d="M0,1038 H440 Q492,1038 515,1104 H0 Z" fill="var(--navy)"/>
  </svg>

  <div class="brand" style="left:31px;top:26px">
    <div class="brand-mark" style="width:48px;height:48px"></div>
  </div>
  <div class="brand-name" style="left:90px;top:40px;font-size:11.2px">BRUSHLINE COATINGS</div>
  <div class="brand-tag" style="left:90px;top:56px;font-size:7.3px">Commercial and Industrial Painting, Epoxy floors and Linemarking</div>

  <div class="welcome">
    <div class="lead">WELCOME TO</div>
    <div class="name accent">BRUSHLINE</div>
    <div class="name">COATINGS</div>
  </div>

  <div class="divider"></div>
  <div class="service-area">
    <strong>We service</strong>
    Sydney, Central Coast,<br>Newcastle, Hunter and<br>Regional NSW.
  </div>

  <div class="footer-item" style="left:34px">
    <svg viewBox="0 0 12 12" fill="none" stroke="#f6d823" stroke-width="1"><circle cx="6" cy="6" r="5"/><ellipse cx="6" cy="6" rx="2.2" ry="5"/><path d="M1 6h10M2 3.3h8M2 8.7h8"/></svg>
    <span>www.<b>brushlinecoatings</b>.com.au</span>
  </div>
  <div class="footer-item" style="left:293px">
    <svg viewBox="0 0 12 12" fill="none" stroke="#f6d823" stroke-width="1"><path d="M3 1.2 4.6 3.6 3.6 4.8Q4.6 7 7.2 8.4L8.4 7.4 10.8 9 9.8 10.8Q5.6 10.6 1.2 3.2Z"/></svg>
    <span>Call us <b>1300 555 019</b></span>
  </div>
</section>

<!-- BACK SIDE -->
<section class="flyer back">
  <svg class="art" viewBox="0 0 852 1104" preserveAspectRatio="none">
    <defs>
      <linearGradient id="floor" x1="0" y1="0" x2="1" y2="1"><stop offset="0" stop-color="#e9ecf0"/><stop offset=".5" stop-color="#f6f7f9"/><stop offset="1" stop-color="#eceef2"/></linearGradient>
      <linearGradient id="panelBlue" x1="0" y1="0" x2="1" y2="1"><stop offset="0" stop-color="#2d7fcc"/><stop offset="1" stop-color="#1b56a4"/></linearGradient>
      <linearGradient id="bandBlue" x1="0" y1="0" x2="1" y2="0"><stop offset="0" stop-color="#1b56a4"/><stop offset=".6" stop-color="#2aa3df"/><stop offset="1" stop-color="#1f6cc0"/></linearGradient>
      <linearGradient id="phWare" x1="0" y1="0" x2="0" y2="1"><stop offset="0" stop-color="#6b5f55"/><stop offset=".5" stop-color="#a39c93"/><stop offset="1" stop-color="#d8d9db"/></linearGradient>
      <linearGradient id="phScaf" x1="0" y1="0" x2="1" y2="1"><stop offset="0" stop-color="#d8dade"/><stop offset=".5" stop-color="#b9875a"/><stop offset="1" stop-color="#8e6a4b"/></linearGradient>
      <linearGradient id="phHeritage" x1="0" y1="0" x2="1" y2="0"><stop offset="0" stop-color="#f3f4f6" stop-opacity="0"/><stop offset=".35" stop-color="#c9bcae"/><stop offset="1" stop-color="#a4613f"/></linearGradient>
      <linearGradient id="footerPhoto" x1="0" y1="0" x2="1" y2="0"><stop offset="0" stop-color="#6f6a66"/><stop offset=".5" stop-color="#7a5d4c"/><stop offset="1" stop-color="#6a4533"/></linearGradient>
    </defs>
    <rect role="img" aria-label="Photo: freshly linemarked carpark floor, faded as background" width="852" height="1104" fill="url(#floor)"/>
    <polygon role="img" aria-label="Photo: painter at work in a blue-toned interior" points="0,0 305,0 305,250 0,350" fill="url(#panelBlue)"/>
    <polygon role="img" aria-label="Photo: warehouse interior with new epoxy floor and mezzanine" points="313,0 612,0 612,170 553,150 313,242" fill="url(#phWare)"/>
    <polygon role="img" aria-label="Photo: painter on scaffolding beside a brick building" points="620,0 852,0 852,262 620,180" fill="url(#phScaf)"/>
    <polygon points="0,342 553,152 852,258 852,312 553,192 0,374" fill="url(#bandBlue)"/>
    <polygon points="0,374 553,192 852,312 852,322 553,204 0,386" fill="#fff" opacity=".8"/>
    <polygon role="img" aria-label="Photo: restored heritage sandstone and brick building" points="470,1038 470,990 620,900 700,830 852,815 852,1038" fill="url(#phHeritage)"/>
    <rect x="430" y="1038" width="422" height="66" fill="url(#footerPhoto)"/>
    <path d="M0,1038 H440 Q492,1038 515,1104 H0 Z" fill="var(--navy)"/>
  </svg>

  <h2 class="services-title">LIST OF <b>OUR</b><span class="accent">SERVICES</span><span class="pointer"></span></h2>

  <div class="service-card" style="left:40px;top:218px">
    <div class="service-icon"><svg viewBox="0 0 30 30"><rect x="9" y="4" width="16" height="7" rx="1.5"/><path d="M17 11v3H10v5"/><rect x="8" y="19" width="4" height="8" rx="1"/></svg></div>
    <p class="service-text">Painting to internal common areas, carparks and foyers</p>
  </div>
  <div class="service-card" style="left:184px;top:218px">
    <div class="service-icon"><svg viewBox="0 0 30 30"><path d="M3 26V13l8-5 8 5v13M3 26h24M19 26V10l8-3v19"/><path d="M7 17h8M7 21h8"/></svg></div>
    <p class="service-text">Painting<br>to external<br>facades</p>
  </div>
  <div class="service-card" style="left:327px;top:218px">
    <div class="service-icon"><svg viewBox="0 0 30 30"><path d="M3 12 15 5l12 7v14H3Z"/><rect x="7" y="15" width="7" height="4" rx="1"/><rect x="16" y="15" width="7" height="4" rx="1"/><rect x="7" y="21" width="7" height="4" rx="1"/><rect x="16" y="21" width="7" height="4" rx="1"/></svg></div>
    <p class="service-text">Carpark and loading dock linemarking and epoxy flooring</p>
  </div>
  <div class="service-card" style="left:40px;top:371px">
    <div class="service-icon"><svg viewBox="0 0 30 30"><path d="M11 6 8 26M19 6l3 20M10 11h10M9.5 16h11M9 21h12M5 4v7M3 9l2 2 2-2M25 11V4M23 6l2-2 2 2"/></svg></div>
    <p class="service-text">Non slip walkways for pedestrian and vehicle traffic</p>
  </div>
  <div class="service-card" style="left:184px;top:371px">
    <div class="service-icon"><svg viewBox="0 0 30 30"><rect x="5" y="5" width="5" height="20" rx="1"/><rect x="12.5" y="5" width="5" height="20" rx="1"/><rect x="20" y="5" width="5" height="20" rx="1"/><path d="M5 11h5M12.5 11h5M20 11h5M5 17h5M12.5 17h5M20 17h5M3 26h24"/></svg></div>
    <p class="service-text">Speed<br>humps, bollard<br>installation</p>
  </div>
  <div class="service-card" style="left:327px;top:371px">
    <div class="service-icon"><svg viewBox="0 0 30 30"><path d="M6 24 19 11M17 6a5 5 0 0 0 7 7l-2-2-1-3-3-1Z"/><path d="M6 6l4 1 13 13-3 3L7 10Z"/></svg></div>
    <p class="service-text">Non structural building, maintenance and repairs</p>
  </div>

  <div class="brand-panel" style="width:268px"></div>
  <div class="brand" style="left:42px;top:507px">
    <div class="brand-mark" style="width:44px;height:44px"></div>
  </div>
  <div class="brand-name" style="left:95px;top:521px;font-size:10px">BRUSHLINE COATINGS</div>
  <div class="brand-tag" style="left:95px;top:536px;font-size:5.6px">Commercial and Industrial Painting, Epoxy floors and Linemarking</div>

  <div class="footer-item" style="left:34px">
    <svg viewBox="0 0 12 12" fill="none" stroke="#f6d823" stroke-width="1"><circle cx="6" cy="6" r="5"/><ellipse cx="6" cy="6" rx="2.2" ry="5"/><path d="M1 6h10M2 3.3h8M2 8.7h8"/></svg>
    <span>www.<b>brushlinecoatings</b>.com.au</span>
  </div>
  <div class="footer-item" style="left:293px">
    <svg viewBox="0 0 12 12" fill="none" stroke="#ffffff" stroke-width="1"><path d="M3 1.2 4.6 3.6 3.6 4.8Q4.6 7 7.2 8.4L8.4 7.4 10.8 9 9.8 10.8Q5.6 10.6 1.2 3.2Z"/></svg>
    <span>Call us <b>1300 555 019</b></span>
  </div>
</section>

</body>
</html>
```